Veltrano - Mechanic/Collision Center Business Card

We're looking for a business card design for our mechanic/ collision repair shop.

Can be with colours or monochromatic.

See the attached files.

Many thanks

```html
<!DOCTYPE html>
<html lang="pt">
<head>
<meta charset="utf-8">
<title>Veltrano – Business Card</title>
<link href="https://fonts.googleapis.com/css2?family=Exo+2:ital,wght@0,400;0,500;0,800;1,800&display=swap" rel="stylesheet">
<style>
  :root {
    --page: #2a2c2f;
    --card-dark: #1d2125;
    --blue: #1e9fd9;
    --blue-light: #a9cfee;
    --white: #ffffff;
    --ink: #1d2125;
    --text-light: #eef1f4;
    --illustration-top: #f4f6f8;
    --illustration-bottom: #d9dee3;
  }
  * { margin: 0; padding: 0; box-sizing: border-box; }
  html, body {
    width: 1200px; height: 900px; overflow: hidden;
    background: var(--page);
    font-family: "Exo 2", sans-serif;
  }
  .sheet {
    width: 1200px; height: 900px;
    display: flex; flex-direction: column; align-items: center; justify-content: center;
    gap: 34px;
  }
  .card {
    width: 720px; height: 400px; position: relative; overflow: hidden;
    box-shadow: 0 16px 30px rgba(0,0,0,.45);
  }

  /* Front */
  .card-front { background: var(--card-dark); }
  .front-illustration {
    position: absolute; left: 150px; top: 70px; width: 440px; height: 190px;
    background: linear-gradient(var(--illustration-top), var(--illustration-bottom));
    border-radius: 60px 60px 8px 8px;
  }
  .band-blue {
    position: absolute; left: 0; right: 0; top: 240px; height: 70px; background: var(--blue);
  }
  .band-light {
    position: absolute; left: 0; right: 0; top: 270px; height: 90px; background: var(--blue-light);
  }
  .band-blue-low {
    position: absolute; left: 0; right: 0; top: 250px; height: 40px; background: var(--blue);
  }

  /* Back */
  .card-back { background: var(--card-dark); display: flex; }
  .brand-panel {
    width: 315px; height: 100%; background: var(--white);
    display: flex; align-items: center; justify-content: center; gap: 12px;
  }
  .brand-mark { width: 26px; height: 26px; background: var(--blue); border-radius: 50%; }
  .brand-name {
    font-weight: 800; font-size: 46px; color: var(--ink); letter-spacing: 1px; text-transform: uppercase;
  }
  .divider-stripe { width: 12px; height: 100%; margin-left: 12px; background: var(--blue); }
  .details { padding: 56px 0 0 56px; color: var(--text-light); }
  .person-name {
    font-weight: 800; font-style: italic; font-size: 30px; color: var(--blue);
    text-transform: uppercase; letter-spacing: 1px; line-height: 1;
  }
  .person-role { font-size: 17px; margin-top: 2px; }
  .contact-list { list-style: none; margin-top: 42px; }
  .contact-item {
    display: flex; align-items: center; gap: 12px; font-size: 19px; line-height: 27px; letter-spacing: .5px;
  }
  .contact-icon { width: 18px; height: 18px; flex: none; }
  .address { margin-top: 36px; font-size: 21px; line-height: 24px; letter-spacing: .8px; }
</style>
</head>
<body>
<main class="sheet">
  <section class="card card-front" aria-label="Card front">
    <div class="band-light"></div>
    <div class="band-blue"></div>
    <div class="front-illustration" role="img" aria-label="Illustration of four white cars side by side with a wrench at the centre"></div>
  </section>

  <section class="card card-back" aria-label="Card back">
    <div class="brand-panel">
      <span class="brand-mark"></span>
      <span class="brand-name">Veltrano</span>
    </div>
    <div class="divider-stripe"></div>
    <div class="details">
      <h1 class="person-name">Rui Matos</h1>
      <p class="person-role">Manager</p>
      <ul class="contact-list">
        <li class="contact-item">
          <svg class="contact-icon" viewBox="0 0 20 20" fill="none" stroke="var(--blue)" stroke-width="1.6"><circle cx="10" cy="10" r="8.5"/><path d="M7 6l1.5 2.5-1 1c.6 1.4 1.6 2.4 3 3l1-1L14 13l-1 1.5c-3.5-.5-6-3-6.5-6.5z"/></svg>
          +351 214550218
        </li>
        <li class="contact-item">
          <svg class="contact-icon" viewBox="0 0 20 20" fill="none" stroke="var(--blue)" stroke-width="1.6"><rect x="6" y="2" width="8" height="16" rx="1.5"/><line x1="9" y1="15" x2="11" y2="15"/></svg>
          +351 912480375
        </li>
        <li class="contact-item">
          <svg class="contact-icon" viewBox="0 0 20 20" fill="none" stroke="var(--blue)" stroke-width="1.6"><rect x="2" y="5" width="16" height="11" rx="1"/><path d="M2 5l8 6 8-6"/></svg>
          veltrano.oficina@mail.com
        </li>
        <li class="contact-item">
          <svg class="contact-icon" viewBox="0 0 20 20"><circle cx="10" cy="10" r="9" fill="var(--blue)"/></svg>
          www.veltrano-oficina.pt
        </li>
      </ul>
      <p class="address">Rua das Oficinas, 42<br>1900-118 Lisboa</p>
    </div>
  </section>
</main>
</body>
</html>
```